Lumora App | Pre-Launch Homepage

Dear designer,
Lumora is a soon to be launched innovative & free social platform for collaborative addictions quitting.
We require a design for our pre-launch homepage that will elevate our basic wireframes to the next level.
We would like the wireframes to serve as a guideline only, and not as a final version of the design. If you have cool ideas - we would appreciate your creativity!
* This is a pre-launch website for a mobile app, and as such the design must be consistent with the general style, design and atmosphere of the app (see screenshot in the shared Drive link).
* We liked the style and feel of the following website: http://palvexapp.com/ - Please let's use it as a reference as well.
* The existing text in the wireframes is there just to represent a place for text. Copy will be edited by us after the design is done.
Please find the wireframes attached, and all relevant design assets and app screenshots in the following Drive shared link -
https://files.norvakshare.com/open?id=7Q284KtP3mXcRf8Hj21W5vLzDne
Thanks,
Marcus
Industry/Entity Type
Social
Number of Pages Required
1 page
Look and feel
Each slider illustrates characteristics of the customer's brand and the style your logo design should communicate.

```html
<!DOCTYPE html>
<html lang="en">
<head>
<meta charset="utf-8">
<title>Lumora App | Pre-Launch Homepage</title>
<link href="https://fonts.googleapis.com/css2?family=Open+Sans:wght@300;400;600&family=Lato:wght@300;400;700&display=swap" rel="stylesheet">
<style>
  :root {
    --ink: #3b3b3b;
    --muted: #6a6a6a;
    --dark: #262626;
    --panel: #2b2b2b;
    --green: #7cc242;
    --green-dark: #5ea52b;
    --line: #bdb6ad;
    --device: #555555;
    --digit: #3a3a3a;
    --bg-top: #fdf7e4;
    --bg-mid: #f9dcc6;
    --bg-low: #f6e9dc;
    --bg-end: #e9dbe8;
  }
  * { box-sizing: border-box; margin: 0; padding: 0; }
  html, body { width: 1200px; height: 3120px; overflow: hidden; }
  body {
    position: relative;
    font-family: "Open Sans", "Helvetica Neue", Arial, sans-serif;
    color: var(--ink);
    background: linear-gradient(180deg, var(--bg-top) 0%, var(--bg-mid) 12%, #f8e3c9 30%, var(--bg-low) 50%, #f7e6d0 70%, var(--bg-end) 92%);
  }
  .abs { position: absolute; }
  .center { left: 0; width: 1200px; text-align: center; }

  /* header */
  .brand { top: 40px; font-family: "Lato", sans-serif; font-size: 64px; font-weight: 700; color: var(--dark); letter-spacing: 1px; }
  .phone-contact { top: 24px; right: 110px; display: flex; align-items: center; gap: 10px; font-size: 13px; color: var(--dark); }
  .tagline { top: 178px; font-size: 19px; line-height: 30px; color: var(--ink); }

  /* subscribe */
  .subscribe { top: 290px; left: 180px; width: 840px; height: 128px; background: var(--panel); padding: 18px 28px; color: #eee; }
  .subscribe p { font-size: 18px; margin-bottom: 14px; }
  .subscribe-row { display: flex; gap: 16px; }
  .email-field { width: 540px; height: 52px; background: #f2f2f2; border: 1px solid #ccc; color: #888; font-size: 17px; padding: 0 16px; line-height: 52px; }
  .notify-button { width: 200px; height: 52px; background: linear-gradient(var(--green), var(--green-dark)); color: #fff; font-size: 17px; font-weight: 600; text-align: center; line-height: 52px; border-radius: 3px; }

  .showcase { top: 470px; left: 360px; width: 480px; height: 320px; background: linear-gradient(160deg, #3a3a3a, #8a8a8a 55%, #e8e8e8); border-radius: 10px; }
  .slider-dots { top: 816px; display: flex; justify-content: center; gap: 10px; }
  .slider-dots span { width: 11px; height: 11px; border-radius: 50%; background: #d8d3cc; border: 1px solid #aaa; }
  .slider-dots span.active { background: #777; }

  /* features */
  .features { top: 900px; left: 110px; width: 980px; display: flex; justify-content: space-between; }
  .feature { width: 280px; text-align: center; }
  .feature-icon { width: 100px; height: 100px; margin: 0 auto 20px; border-radius: 50%; }
  .feature h3 { font-family: "Lato", sans-serif; font-weight: 400; font-size: 30px; color: var(--dark); margin-bottom: 14px; }
  .feature p { font-size: 13px; line-height: 19px; color: var(--muted); width: 190px; margin: 0 auto; }

  /* fun */
  .fun-device { top: 1240px; left: 150px; }
  .fun-title { top: 1200px; left: 560px; width: 360px; text-align: center; font-size: 56px; font-weight: 300; color: var(--dark); }
  .fun-copy { top: 1330px; left: 690px; width: 380px; font-size: 13px; line-height: 21px; color: var(--muted); }
  .fun-copy p + p { margin-top: 24px; }
  .divider { top: 1690px; left: 150px; width: 900px; height: 1px; background: var(--line); }

  /* achieve */
  .achieve-title { top: 1722px; font-size: 56px; font-weight: 300; color: var(--dark); }
  .achieve-copy { top: 1830px; left: 310px; width: 580px; text-align: center; font-size: 18px; line-height: 28px; color: var(--ink); }
  .achieve-strap { top: 1908px; font-size: 18px; color: var(--ink); }
  .achieve-device { top: 2040px; left: 480px; }
  .reward { width: 300px; display: flex; align-items: center; gap: 18px; font-size: 11px; line-height: 16px; color: var(--muted); }
  .reward.right { flex-direction: row; }
  .trophy { width: 50px; height: 58px; flex: none; background: linear-gradient(#f5d66a, #d8a62a); border-radius: 6px 6px 14px 14px; }

  /* coming soon */
  .soon-title { top: 2490px; font-size: 54px; font-weight: 300; color: var(--dark); }
  .nav-arrow { top: 2685px; width: 54px; height: 54px; border: 2px solid #555; border-radius: 50%; }
  .countdown { display: flex; align-items: center; gap: 14px; }
  .countdown-badge { width: 70px; height: 70px; border-radius: 50%; }
  .digits { display: flex; gap: 8px; align-items: center; }
  .digits span { display: inline-block; width: 32px; height: 46px; background: var(--digit); color: #eee; font-family: "Lato", sans-serif; font-weight: 700; font-size: 28px; text-align: center; line-height: 46px; border-radius: 3px; }
  .digits b { color: var(--digit); font-size: 24px; }

  /* footer */
  .site-footer { top: 2860px; left: 0; width: 1200px; height: 260px; background: var(--dark); color: #ddd; text-align: center; }
  .site-footer h2 { margin-top: 40px; font-size: 40px; font-weight: 300; color: #fff; }
  .social-links { display: flex; justify-content: center; gap: 20px; margin-top: 28px; }
  .social-links span { width: 44px; height: 44px; border-radius: 50%; background: #f2f2f2; }
  .copyright { margin-top: 26px; font-size: 12px; color: #aaa; }
  .footer-links { margin-top: 14px; font-size: 12px; color: #aaa; }
</style>
</head>
<body>

<header>
  <div class="abs center brand">Lumora</div>
  <div class="abs phone-contact">
    <svg width="22" height="22" viewBox="0 0 24 24"><path fill="#262626" d="M6.6 10.8a15 15 0 0 0 6.6 6.6l2.2-2.2c.3-.3.7-.4 1-.2 1.1.4 2.3.6 3.6.6.6 0 1 .4 1 1V20c0 .6-.4 1-1 1A17 17 0 0 1 3 4c0-.6.4-1 1-1h3.5c.6 0 1 .4 1 1 0 1.3.2 2.5.6 3.6.1.3 0 .7-.2 1z"/></svg>
    <span>+1 555 0190</span>
  </div>
  <p class="abs center tagline">Lumora is a revolutionary &amp; free social platform for collaborative<br>addictions quitting.</p>
</header>

<section class="abs subscribe">
  <p>Subscribe below for the beta release and updates</p>
  <div class="subscribe-row">
    <div class="email-field">Enter Your Email...</div>
    <div class="notify-button">LET ME KNOW!</div>
  </div>
</section>

<div class="abs showcase" role="img" aria-label="App shown on desktop monitor, laptop, tablet and phone"></div>
<div class="abs center slider-dots"><span class="active"></span><span></span><span></span></div>

<section class="abs features">
  <div class="feature">
    <div class="feature-icon" role="img" aria-label="Red and white lifebuoy icon" style="background:radial-gradient(circle,#fff 0 30%,#d9423a 31% 70%,transparent 71%)"></div>
    <h3>Never be Alone</h3>
    <p>Forget what you know - Lumora makes it fun to quit.</p>
  </div>
  <div class="feature">
    <div class="feature-icon" role="img" aria-label="Golden star icon" style="background:radial-gradient(circle,#f3cf55 0 45%,#d8a42c 46% 60%,transparent 61%)"></div>
    <h3>Network Power</h3>
    <p>Forget what you know - Lumora makes it fun to quit.</p>
  </div>
  <div class="feature">
    <div class="feature-icon" role="img" aria-label="Black feathered headdress icon" style="background:radial-gradient(circle,#3a3a3a 0 50%,#8a8a8a 51% 65%,transparent 66%)"></div>
    <h3>Stay Motivated</h3>
    <p>Forget what you know - Lumora makes it fun to quit.</p>
  </div>
</section>

<section class="fun">
  <svg class="abs fun-device" width="240" height="420" viewBox="0 0 240 420">
    <rect x="4" y="4" width="232" height="412" rx="26" fill="var(--device)"/>
    <rect x="20" y="54" width="200" height="290" fill="#fafafa"/>
    <circle cx="120" cy="380" r="16" fill="none" stroke="#fff" stroke-width="3"/>
    <rect x="24" y="58" width="192" height="282" fill="#fbe9e4" role="img" aria-label="Line drawing of a smiling baby"/>
  </svg>
  <h2 class="abs fun-title">Fun</h2>
  <div class="abs fun-copy">
    <p>Forget what you know - Lumora makes it fun to quit. The battle between your good and bad demons comes to life in our gamified approach for managing your campaigns.</p>
    <p>Lumora gives you the opportunity to take an active role in helping your network to smash your common addictions as a team. That's right, we converted the cessation process into a social game.</p>
  </div>
  <div class="abs divider"></div>
</section>

<section class="achieve">
  <h2 class="abs center achieve-title">Achieve</h2>
  <p class="abs achieve-copy">Lumora is built as a pyramid of relationships that makes use of the Social Cognitive Theory, to provide a powerful network of positive reinforcement.</p>
  <p class="abs center achieve-strap">The bigger you make it the stronger you get</p>

  <div class="abs reward" style="top:2100px;left:130px;"><span>Lorem Ipsum is simply dummy text of the printing and typesetting industry. Lorem Ipsum simply.</span><div class="trophy" role="img" aria-label="Gold trophy"></div></div>
  <div class="abs reward" style="top:2280px;left:130px;"><span>Lorem Ipsum is simply dummy text of the printing and typesetting industry. Lorem Ipsum simply.</span><div class="trophy" role="img" aria-label="Gold trophy"></div></div>
  <div class="abs reward right" style="top:2100px;left:740px;"><div class="trophy" role="img" aria-label="Gold trophy"></div><span>Lorem Ipsum is simply dummy text of the printing and typesetting industry. Lorem Ipsum simply.</span></div>
  <div class="abs reward right" style="top:2280px;left:740px;"><div class="trophy" role="img" aria-label="Gold trophy"></div><span>Lorem Ipsum is simply dummy text of the printing and typesetting industry. Lorem Ipsum simply.</span></div>

  <svg class="abs achieve-device" width="240" height="400" viewBox="0 0 240 400">
    <rect x="4" y="4" width="232" height="392" rx="26" fill="var(--device)"/>
    <rect x="20" y="50" width="200" height="280" fill="#fafafa"/>
    <circle cx="120" cy="362" r="16" fill="none" stroke="#fff" stroke-width="3"/>
    <rect x="24" y="54" width="192" height="272" fill="#f6ecd0" role="img" aria-label="Gold medal on a blue ribbon"/>
  </svg>
</section>

<section class="coming-soon">
  <h2 class="abs center soon-title">Coming Soon</h2>
  <div class="abs nav-arrow" style="left:190px;">
    <svg width="50" height="50" viewBox="0 0 50 50"><path d="M28 16 L19 25 L28 34" fill="none" stroke="#555" stroke-width="3"/></svg>
  </div>
  <div class="abs nav-arrow" style="left:956px;">
    <svg width="50" height="50" viewBox="0 0 50 50"><path d="M22 16 L31 25 L22 34" fill="none" stroke="#555" stroke-width="3"/></svg>
  </div>
  <div class="abs countdown" style="top:2640px;left:320px;">
    <div class="countdown-badge" role="img" aria-label="Yellow achievement badge" style="background:#f0cf4e"></div>
    <div class="digits"><span>0</span><span>0</span><b>:</b><span>1</span><span>1</span><b>:</b><span>1</span><span>4</span><b>:</b><span>3</span><span>0</span><b>:</b><span>1</span><span>0</span></div>
    <div class="countdown-badge" role="img" aria-label="Red crossed-out badge" style="background:#d9423a"></div>
  </div>
  <div class="abs countdown" style="top:2738px;left:370px;">
    <div class="countdown-badge" role="img" aria-label="Round profile badge" style="width:50px;height:50px;background:#8a6e5a"></div>
    <div class="digits"><span>0</span><span>0</span><b>:</b><span>1</span><span>1</span><b>:</b><span>1</span><span>4</span><b>:</b><span>3</span><span>0</span><b>:</b><span>0</span><span>0</span></div>
  </div>
</section>

<footer class="abs site-footer">
  <h2>Join the Revolution</h2>
  <div class="social-links"><span></span><span></span><span></span></div>
  <p class="copyright">Copyright © 2014 Lumora Ltd.</p>
  <p class="footer-links">Contact Us | T&amp;C's | Privacy Policy</p>
</footer>

</body>
</html>
```